Engineering and Energy service provider

We need a design that gives the impression of a high level of technical competence and a reliable partner. Simple structure with little need for updates.
The company brand is Volnar and today consists of two main businesses: energy optimisation (Volnar energy) and technical consultancy (Volnar Engineering). Volnar energy is shown in the attached powerpoint,
We are a young growing company that consists of several businesses, the largest parts are energy monitoring services and consulting services. Consulting services for commercial installations in the technical area of cooling, ventilation, heating and energy. Services offered include project planning, project management, inspection, operational analysis and technical investigations. Energy monitoring and optimization services are performed as a subscription with a subscription to the service.
Target Market(s)
Commercial property owners Grocery retail, grocery stores, construction companies
Industry/Entity Type
energy services and consulting services
Coding
Coded - Design and coding required
Number of Pages Required
5+ page
Look and feel
Each slider illustrates characteristics of the customer's brand and the style your logo design should communicate.

```html
<!DOCTYPE html>
<html lang="en">
<head>
<meta charset="utf-8">
<title>Volnar Energy</title>
<link href="https://fonts.googleapis.com/css2?family=Open+Sans:wght@400;600;700&family=Lato:wght@400;700&display=swap" rel="stylesheet">
<style>
:root{
  --blue:#0a4ea3;
  --blue-dark:#083d82;
  --navy:#0b2f6e;
  --ink:#1a1a1a;
  --muted:#6b6b6b;
  --grey:#e8eaec;
  --card:#e3e6e9;
  --footer:#232323;
  --white:#fff;
}
*{box-sizing:border-box;margin:0;padding:0}
html,body{width:1200px;height:3852px;overflow:hidden}
body{position:relative;background:var(--white);font-family:"Lato",sans-serif;color:var(--ink)}
.abs{position:absolute}
h1,h2,h3,.heading{font-family:"Open Sans",sans-serif}
.btn{position:absolute;display:flex;align-items:center;justify-content:center;background:var(--blue);color:var(--white);font-family:"Open Sans",sans-serif;font-weight:700;font-size:16px;border-radius:3px;white-space:nowrap}
.underline{position:absolute;height:4px;background:var(--blue)}
.accent{color:var(--blue);font-weight:700}

/* nav */
.site-nav{position:absolute;left:0;top:0;width:1200px;height:79px;background:var(--white)}
.brand{position:absolute;left:109px;top:20px;font-family:"Open Sans",sans-serif;font-weight:700;font-size:32px;color:var(--blue);letter-spacing:1px}
.nav-links a{position:absolute;top:30px;font-size:15px;color:var(--ink);text-decoration:none;white-space:nowrap}
.nav-home{left:408px!important;top:25px!important;width:63px;height:28px;background:var(--blue);color:#fff!important;border-radius:3px;display:flex;align-items:center;justify-content:center;font-weight:700}
.nav-contact{left:998px;top:20px;width:90px;height:42px}

/* hero */
.hero{position:absolute;left:0;top:79px;width:1200px;height:542px;background:radial-gradient(ellipse at 75% 40%,#2a6bd0 0%,#0d3f94 45%,#062a6a 100%)}
.hero h1{position:absolute;left:109px;top:104px;color:var(--white);font-weight:700;font-size:52px;line-height:68px}
.hero .btn{top:335px;height:48px;font-size:16px}
.hero .btn-light{background:var(--white);color:var(--blue)}

/* about */
.about-photo{left:111px;top:727px;width:444px;height:431px;background:linear-gradient(135deg,#7b7a78,#4a4846 60%,#2e2d2c)}
.about-title{left:643px;top:737px;font-size:45px;font-weight:400}
.about-text{left:643px;top:828px;width:443px;font-size:14px;line-height:29px;color:var(--muted);text-align:justify}
.about-text p+p{margin-top:17px}

/* services */
.services{left:0;top:1269px;width:1200px;height:583px;background:var(--grey)}
.services-title{left:111px;top:1304px;font-size:45px;font-weight:400}
.tab{top:1324px;font-size:17px}
.svc-photo{top:1406px;width:317px;height:329px}
.svc-cap{top:1745px;font-family:"Open Sans",sans-serif;font-size:18px}

/* path */
.path-card{top:1961px;width:211px;height:274px;background:var(--card);padding:18px 14px}
.path-card .icon{width:59px;height:59px;border-radius:50%;background:var(--blue);display:flex;align-items:center;justify-content:center}
.path-card h3{font-weight:400;font-size:19px;margin-top:20px;white-space:nowrap}
.path-card p{font-size:14px;line-height:26px;color:var(--muted);margin-top:6px}
.path-title{left:330px;top:1965px;width:540px;text-align:center;font-size:45px;line-height:52px;font-weight:400}

/* why */
.why-left{left:0;top:2323px;width:645px;height:564px;background:var(--blue)}
.why-photo{left:645px;top:2323px;width:555px;height:564px;background:linear-gradient(160deg,#39506e,#1d2a3b 55%,#3a4a5a)}
.why-title{left:114px;top:2370px;font-size:45px;color:var(--white);font-weight:400}
.why-item{left:115px;display:flex;align-items:center;color:var(--white);font-family:"Open Sans",sans-serif;font-size:20px}
.why-item .circle{width:75px;height:75px;border-radius:50%;background:var(--white);display:flex;align-items:center;justify-content:center;margin-right:24px}

/* contact */
.contact-title{left:0;top:2990px;width:1200px;text-align:center;font-size:45px;font-weight:400}
.field{position:absolute;border:1px solid #c9c9c9;border-radius:4px;background:#f7f7f7;display:flex;align-items:center;padding-left:18px;font-size:14px;color:#666}
.field svg{margin-right:14px}

/* footer */
.site-footer{left:0;top:3531px;width:1200px;height:321px;background:var(--footer)}
.foot-brand{left:111px;top:3612px;font-family:"Open Sans",sans-serif;font-weight:700;font-size:34px;color:var(--blue)}
.social{top:3692px;width:30px;height:30px;border-radius:50%;background:var(--white)}
.foot-head{top:3600px;font-size:18px;color:var(--blue);text-transform:uppercase}
.foot-list{list-style:none;font-size:15px;line-height:25.5px;color:var(--white)}
.foot-info{left:865px;font-size:15px;display:flex;align-items:center;color:var(--white)}
.foot-info svg{margin-right:14px}
.foot-rule{left:111px;top:3812px;width:978px;height:1px;background:#777}
.copyright{left:0;top:3827px;width:1200px;text-align:center;font-size:13px;color:var(--white)}
</style>
</head>
<body>

<header class="site-nav">
  <div class="brand">Volnar Energy</div>
  <nav class="nav-links">
    <a class="nav-home" href="#">Home</a>
    <a style="left:503px" href="#">About Us</a>
    <a style="left:608px" href="#">Services</a>
    <a style="left:704px" href="#">Volnar Energy</a>
    <a style="left:838px" href="#">Volnar Engineering</a>
  </nav>
  <div class="btn nav-contact">Contact</div>
</header>

<section class="hero" role="img" aria-label="Night city skyline overlaid with glowing blue network lines">
  <h1>Engineering precision<br>Monitoring performance<br>Driving energy efficiency</h1>
  <div class="btn" style="left:111px;width:193px">Explore Volnar Energy</div>
  <div class="btn btn-light" style="left:319px;width:236px">Explore Volnar Engineering</div>
</section>

<div class="abs about-photo" role="img" aria-label="Team of engineers discussing parts around a workshop table"></div>
<h2 class="abs about-title">About <span class="accent">Us</span></h2>
<div class="underline" style="left:643px;top:793px;width:114px"></div>
<div class="abs about-text">
  <p>At Volnar Energy, we combine engineering expertise with data-driven insight to help businesses optimize their technical systems and energy performance. Our mission is simple — to deliver smarter, more efficient, and more sustainable operations through precision engineering and continuous monitoring.</p>
  <p>We are a young and growing company built on a foundation of technical excellence and practical experience. Volnar consists of specialized divisions that work seamlessly together:</p>
</div>
<div class="btn" style="left:643px;top:1100px;width:115px;height:48px">Read More</div>

<section class="abs services"></section>
<h2 class="abs services-title">Our <span class="accent">Services</span></h2>
<div class="underline" style="left:111px;top:1367px;width:71px"></div>
<div class="abs tab" style="left:739px">Energy Monitoring</div>
<div class="abs tab accent" style="left:913px;font-family:'Open Sans',sans-serif">Consulting Services</div>
<div class="abs" style="left:912px;top:1363px;width:171px;height:2px;background:var(--blue)"></div>
<div class="abs svc-photo" style="left:109px;background:linear-gradient(160deg,#8a8f94,#5d6166 60%,#b7c23a)" role="img" aria-label="Two site workers in hi-vis jackets reviewing plans in a building under construction"></div>
<div class="abs svc-photo" style="left:440px;background:linear-gradient(160deg,#6f7b86,#3b4a5c 55%,#c9c43a)" role="img" aria-label="Manager in a suit with hard-hat workers checking a clipboard"></div>
<div class="abs svc-photo" style="left:769px;background:linear-gradient(160deg,#a9b9c8,#e06a1e 45%,#3d4a3a)" role="img" aria-label="Worker in orange hard hat holding a tablet at a construction site"></div>
<div class="abs svc-cap" style="left:111px">Construction Planning</div>
<div class="abs svc-cap" style="left:441px">Project Management</div>
<div class="abs svc-cap" style="left:771px">Inspection</div>

<div class="abs path-card" style="left:109px">
  <div class="icon"><svg width="30" height="30" viewBox="0 0 24 24"><path d="M13 2 4 14h7l-1 8 9-12h-7z" fill="#fff"/></svg></div>
  <h3>Volnar Energy</h3>
  <p>Real-time energy monitoring &amp; optimization, delivered as a subscription service.</p>
</div>
<h2 class="abs path-title">Choose Your Path<br><span class="accent">Energy or Engineering</span></h2>
<div class="underline" style="left:564px;top:2086px;width:72px"></div>
<div class="abs" style="left:330px;top:2108px;width:540px;text-align:center;font-size:17px;color:#555">Let users easily navigate to the right business area.</div>
<div class="btn" style="left:543px;top:2153px;width:115px;height:47px">Read More</div>
<div class="abs path-card" style="left:869px">
  <div class="icon"><svg width="32" height="32" viewBox="0 0 24 24"><circle cx="12" cy="12" r="7" fill="none" stroke="#fff" stroke-width="2.4" stroke-dasharray="3 2"/><circle cx="12" cy="12" r="3" fill="#fff"/></svg></div>
  <h3>Volnar Engineering</h3>
  <p>Consulting services for cooling, ventilation, heating, and energy systems.</p>
</div>

<section class="abs why-left"></section>
<div class="abs why-photo" role="img" aria-label="Two engineers in white hard hats and blue overalls checking a tablet beside industrial wiring"></div>
<h2 class="abs why-title"><b>Why Choose</b> Volnar?</h2>
<div class="abs" style="left:116px;top:2435px;width:96px;height:4px;background:var(--white)"></div>
<div class="abs why-item" style="top:2490px"><span class="circle"><svg width="40" height="40" viewBox="0 0 24 24"><circle cx="12" cy="10" r="7" fill="none" stroke="#0a4ea3" stroke-width="2"/><path d="M12 6l1.2 2.5 2.7.3-2 1.9.5 2.7-2.4-1.3-2.4 1.3.5-2.7-2-1.9 2.7-.3z" fill="#0a4ea3"/><path d="M8 16l-1 6 5-2 5 2-1-6" fill="none" stroke="#0a4ea3" stroke-width="2"/></svg></span>Independent expertise</div>
<div class="abs why-item" style="top:2584px"><span class="circle"><svg width="40" height="40" viewBox="0 0 24 24"><path d="M3 19h5l4-6 3 3 6-9" fill="none" stroke="#0a4ea3" stroke-width="2.2"/><path d="M17 7h4v4" fill="none" stroke="#0a4ea3" stroke-width="2.2"/></svg></span>Energy + technical systems in one place</div>
<div class="abs why-item" style="top:2679px"><span class="circle"><svg width="40" height="40" viewBox="0 0 24 24"><circle cx="13" cy="8" r="5" fill="#0a4ea3"/><text x="13" y="11" font-size="7" text-anchor="middle" fill="#fff" font-family="sans-serif">$</text><path d="M2 16h4l5 2h5l4-3v3l-6 4H8l-6-2z" fill="#0a4ea3"/></svg></span>Proven cost savings</div>
<div class="abs why-item" style="top:2773px"><span class="circle"><svg width="40" height="40" viewBox="0 0 24 24" fill="none" stroke="#0a4ea3" stroke-width="2"><path d="M3 9V3h6M21 9V3h-6M3 15v6h6M21 15v6h-6M3 3l6 6M21 3l-6 6M3 21l6-6M21 21l-6-6"/><rect x="9" y="9" width="6" height="6"/></svg></span>Scalable solutions for commercial clients</div>

<h2 class="abs contact-title">Contact <span class="accent">Us</span></h2>
<div class="underline" style="left:564px;top:3056px;width:72px"></div>
<div class="field" style="left:136px;top:3101px;width:452px;height:53px"><svg width="18" height="18" viewBox="0 0 24 24" fill="#999"><circle cx="12" cy="8" r="4"/><path d="M4 21c0-5 4-7 8-7s8 2 8 7z"/></svg>Name</div>
<div class="field" style="left:615px;top:3101px;width:452px;height:48px"><svg width="18" height="18" viewBox="0 0 24 24" fill="none" stroke="#999" stroke-width="2"><rect x="3" y="5" width="18" height="14"/><path d="M3 5l9 7 9-7"/></svg>Email</div>
<div class="field" style="left:136px;top:3176px;width:452px;height:53px"><svg width="18" height="18" viewBox="0 0 24 24" fill="#999"><path d="M6 2l4 4-2 3c1 3 4 6 7 7l3-2 4 4-3 4C10 21 3 14 2 5z"/></svg>Phone</div>
<div class="field" style="left:615px;top:3176px;width:452px;height:48px"><svg width="20" height="20" viewBox="0 0 24 24" fill="none" stroke="#999" stroke-width="2"><circle cx="12" cy="12" r="3"/><circle cx="12" cy="12" r="8" stroke-dasharray="3 2"/></svg>Services</div>
<div class="field" style="left:136px;top:3251px;width:930px;height:112px;align-items:flex-start;padding-top:18px"><svg width="20" height="18" viewBox="0 0 24 24" fill="#999"><path d="M2 4h20v13H8l-5 4v-4H2z"/></svg>Message</div>
<div class="btn" style="left:539px;top:3399px;width:122px;height:46px">Submit Now</div>

<footer class="abs site-footer"></footer>
<div class="abs foot-brand">Volnar Engineering</div>
<div class="abs social" style="left:112px;background:var(--blue)"></div>
<div class="abs social" style="left:146px"></div>
<div class="abs social" style="left:180px"></div>
<div class="abs social" style="left:215px"></div>
<div class="abs social" style="left:253px"></div>
<div class="abs foot-head" style="left:482px">Quick Links</div>
<ul class="abs foot-list" style="left:486px;top:3640px"><li>Home</li><li>About Us</li><li>Services</li><li>Volnar Energy</li><li>Volnar Engineering</li><li>Contact Us</li></ul>
<div class="abs foot-head" style="left:663px">Other Links</div>
<ul class="abs foot-list" style="left:666px;top:3640px;line-height:32.5px"><li>Privacy Policy</li><li>Terms &amp; Conditions</li><li>Disclaimer</li><li>FAQ's</li><li>Support</li></ul>
<div class="abs foot-head" style="left:865px">Contact Info</div>
<div class="abs foot-info" style="top:3645px"><svg width="22" height="22" viewBox="0 0 24 24"><path d="M12 2a7 7 0 0 0-7 7c0 5 7 13 7 13s7-8 7-13a7 7 0 0 0-7-7z" fill="#fff"/><circle cx="12" cy="9" r="2.5" fill="#232323"/></svg>Harbor Lane, USA -582041</div>
<div class="abs foot-info" style="top:3700px"><svg width="22" height="22" viewBox="0 0 24 24"><circle cx="12" cy="12" r="11" fill="#fff"/><path d="M8 6l3 3-1.5 2c.8 1.8 2 3 3.5 3.5l2-1.5 3 3-2 2C10 18 6 13 6 8z" fill="#232323"/></svg>+1 555 014 2270</div>
<div class="abs foot-info" style="top:3755px"><svg width="22" height="22" viewBox="0 0 24 24"><circle cx="12" cy="12" r="11" fill="#fff"/><rect x="6" y="8" width="12" height="8" fill="#232323"/><path d="M6 8l6 4 6-4" fill="none" stroke="#fff" stroke-width="1.2"/></svg>info@volnarenergy.com</div>
<div class="abs foot-rule"></div>
<div class="abs copyright">© 2025 Volnar Energy .All rights reserved</div>

</body>
</html>
```